For a German comparison website comparing the best online trading brokers I need 10 banners for Facebook advertising. The banners should be a size of 1200x628 with one of the following texts:
1) Traden für Anfänger
25 Euro gratis
2) Traden Sie online
25 Euro gratis
3) Online-Trading für Anfänger
4) Trading für Einsteiger
25 Euro gratis
5) Aktien für Einsteiger
25 Euro gratis
The targeted website is www.marvolink.ch and it compares brokers where traders can trade shares, commodities,indices and Forex.

```html
<!DOCTYPE html>
<html lang="de">
<head>
<meta charset="utf-8">
<title>Traden für Anfänger – 25 € gratis</title>
<link rel="stylesheet" href="https://fonts.googleapis.com/css2?family=Krona+One&family=Archivo+Black&display=swap">
<style>
  :root {
    --bg-dark: #2f2f2f;
    --bg-mid: #474747;
    --chart-shape: rgba(255, 255, 255, 0.06);
    --chart-line: rgba(255, 255, 255, 0.08);
    --frame: #ffffff;
    --frame-fill: rgba(40, 40, 40, 0.55);
    --text-light: #ffffff;
    --offer-top: #ffd21f;
    --offer-mid: #ff8a1a;
    --offer-bottom: #e8231f;
    --photo-light: #b9bcc0;
    --photo-dark: #6d7176;
  }
  html, body {
    margin: 0;
    padding: 0;
    overflow: hidden;
  }
  .banner {
    position: relative;
    width: 1200px;
    height: 628px;
    overflow: hidden;
    background: radial-gradient(ellipse at 45% 35%, var(--bg-mid) 0%, var(--bg-dark) 75%);
    font-family: "Krona One", sans-serif;
  }
  .market-chart {
    position: absolute;
    inset: 0;
  }
  .headline-frame {
    position: absolute;
    left: 78px;
    top: 76px;
    width: 604px;
    height: 272px;
  }
  .headline {
    position: absolute;
    left: 128px;
    top: 106px;
    margin: 0;
    color: var(--text-light);
    font-weight: 400;
    font-size: 58px;
    line-height: 70px;
    font-variant: small-caps;
    letter-spacing: 2px;
    text-shadow: 3px 3px 0 rgba(0, 0, 0, 0.5);
  }
  .offer {
    position: absolute;
    left: 118px;
    top: 384px;
    text-align: center;
    font-family: "Archivo Black", sans-serif;
  }
  .offer-amount {
    display: block;
    font-size: 142px;
    line-height: 124px;
    letter-spacing: 4px;
    background: linear-gradient(180deg, var(--offer-top) 0%, var(--offer-mid) 50%, var(--offer-bottom) 100%);
    -webkit-background-clip: text;
    background-clip: text;
    color: transparent;
  }
  .offer-label {
    display: block;
    color: var(--text-light);
    font-size: 80px;
    line-height: 78px;
    letter-spacing: 3px;
  }
  .advisor-photo {
    position: absolute;
    left: 645px;
    top: 74px;
    width: 470px;
    height: 554px;
    border-radius: 200px 200px 0 0;
    background: linear-gradient(180deg, var(--photo-light) 0%, var(--photo-dark) 100%);
  }
</style>
</head>
<body>
<div class="banner">
  <svg class="market-chart" width="1200" height="628" viewBox="0 0 1200 628" aria-hidden="true">
    <g fill="var(--chart-shape)">
      <rect x="10" y="520" width="50" height="108"/>
      <rect x="480" y="440" width="46" height="188"/>
      <rect x="540" y="400" width="46" height="228"/>
      <rect x="600" y="470" width="46" height="158"/>
      <rect x="1000" y="330" width="46" height="298"/>
      <rect x="1060" y="400" width="46" height="228"/>
      <rect x="1120" y="360" width="46" height="268"/>
    </g>
    <path d="M0 40 C 220 20, 300 220, 520 260 S 820 140, 1040 40"
          fill="none" stroke="var(--chart-line)" stroke-width="60"/>
    <path d="M900 230 L1040 70 L1060 200 Z" fill="var(--chart-shape)"/>
  </svg>

  <svg class="headline-frame" width="604" height="272" viewBox="0 0 604 272" aria-hidden="true">
    <path d="M32 3 H601 V238 L567 269 H3 V34 Z"
          fill="var(--frame-fill)" stroke="var(--frame)" stroke-width="5"/>
  </svg>

  <h1 class="headline">Traden<br>für<br>Anfänger</h1>

  <p class="offer">
    <span class="offer-amount">25 €</span>
    <span class="offer-label">GRATIS</span>
  </p>

  <div class="advisor-photo" role="img" aria-label="Smiling businessman in a grey suit and blue tie, pointing to the headline"></div>
</div>
</body>
</html>
```